Business card design needed

I am looking for a simple but elegant business card that has a professional and a classy look and feel about it. Must engage the persons attention.
I own and run multiple dental practices and offer basic to advanced dentistry.

Target Market(s)

people looking for dentists

Industry/Entity Type

Dental

Contact Information for Business Card

Dr. Leopold Harwick
Bluefern Dental
Your Smile My Passion
Rockhampton - 14 Tindale Street Ph: 0749511862
Emerald - 27 Corbel Street Ph: 0749306417
Calliope - Shop 3 42 Pellow Drive Ph: 49628473
Email: lh@blueferndental.com.au

Requirements
Must have
• Contact Details
QR codes for easy storage and website redirection
email and web address

```html
<!DOCTYPE html>
<html lang="en">
<head>
<meta charset="utf-8">
<title>Bluefern Dental – Business Card</title>
<link rel="stylesheet" href="https://fonts.googleapis.com/css2?family=Arimo:wght@400;700&family=Tinos:wght@700&family=Cormorant+Garamond:ital,wght@1,500&display=swap">
<style>
  :root {
    --paper: #ffffff;
    --ink: #111111;
    --teal-deep: #005753;
    --teal: #0f8a86;
    --frame: #1a1a1a;
  }
  * { margin: 0; padding: 0; box-sizing: border-box; }
  html, body { width: 1200px; height: 590px; overflow: hidden; background: var(--paper); }
  body { position: relative; font-family: "Arimo", Arial, sans-serif; color: var(--ink); }

  .card { position: absolute; width: 363px; height: 211px; border: 1px solid var(--frame); background: var(--paper); overflow: hidden; }
  .card--front { left: 247px; top: 87px; }
  .card--back { left: 697px; top: 84px; }

  /* Front: brand header */
  .brand-head { position: absolute; left: 0; top: 0; width: 100%; height: 103px; }
  .brand-dot { position: absolute; left: 68px; top: 14px; width: 56px; height: 56px; border-radius: 50%; background: var(--teal); }
  .brand-name { position: absolute; left: 134px; top: 26px; font-family: "Tinos", "Times New Roman", serif; font-weight: 700; font-size: 28px; line-height: 32px; color: var(--teal); white-space: nowrap; }
  .tagline { position: absolute; left: 0; top: 84px; width: 100%; text-align: center; font-size: 15px; line-height: 17px; color: var(--ink); }
  .tagline em { font-style: normal; color: var(--teal); }

  /* Front: contact panel */
  .contact-panel { position: absolute; left: 0; top: 103px; width: 100%; height: 108px; background: var(--teal-deep); color: var(--paper); font-size: 11px; }
  .doctor { position: absolute; left: 9px; top: 8px; font-size: 19px; font-weight: 400; line-height: 22px; }
  .practice { position: absolute; line-height: 14px; }
  .practice--rock { left: 8px; top: 54px; }
  .practice--emerald { left: 223px; top: 29px; font-size: 10.5px; }
  .practice--calliope { left: 223px; top: 61px; width: 134px; font-size: 10.5px; }
  .divider { position: absolute; left: 222px; top: 58px; width: 135px; height: 1px; background: var(--paper); }
  .line { display: flex; align-items: center; gap: 5px; white-space: nowrap; }
  .email { position: absolute; left: 8px; top: 90px; }
  .icon { width: 12px; height: 12px; flex: none; }

  /* Back */
  .side-band { position: absolute; left: 0; top: 0; width: 78px; height: 100%; background: var(--teal-deep); }
  .side-name { position: absolute; left: 39px; top: 50%; transform: translate(-50%, -50%) rotate(-90deg); font-family: "Tinos", "Times New Roman", serif; font-weight: 700; font-size: 25px; color: var(--ink); white-space: nowrap; }
  .stripe { position: absolute; top: 0; height: 100%; width: 3px; background: var(--teal); }
  .stripe--a { left: 80px; }
  .stripe--b { left: 86px; }
  .back-mark { position: absolute; left: 152px; top: 18px; width: 128px; height: 128px; border-radius: 50%; border: 3px solid var(--teal); }
  .back-tagline { position: absolute; left: 96px; top: 170px; width: 240px; text-align: center; font-family: "Cormorant Garamond", Georgia, serif; font-style: italic; font-weight: 500; font-size: 20px; line-height: 24px; color: var(--ink); }
</style>
</head>
<body>
  <section class="card card--front">
    <header class="brand-head">
      <span class="brand-dot" aria-hidden="true"></span>
      <span class="brand-name">Bluefern Dental</span>
      <p class="tagline">Beautiful <em>smiles</em> are made here</p>
    </header>
    <div class="contact-panel">
      <h1 class="doctor">Dr. Leopold Harwick</h1>
      <div class="practice practice--rock">
        <div class="line">Rockhampton – 14 Tindale Street</div>
        <div class="line"><svg class="icon" viewBox="0 0 12 12"><circle cx="6" cy="6" r="6" fill="#fff"/><path d="M4 3.2l1 1.6-.6.7c.4.9 1 1.5 1.9 1.9l.7-.6 1.6 1-.6 1.2C6 8.8 3.2 6 3 3.8z" fill="#005753"/></svg>0749511862</div>
      </div>
      <div class="line email"><svg class="icon" viewBox="0 0 14 10" style="width:16px"><rect x="0.5" y="0.5" width="13" height="9" fill="#fff" stroke="#888"/><path d="M.5.5L7 6 13.5.5" fill="none" stroke="#666"/></svg>lh@blueferndental.com.au</div>
      <div class="practice practice--emerald">
        <div class="line">Emerald – 27 Corbel Street</div>
        <div class="line"><svg class="icon" viewBox="0 0 12 12"><circle cx="6" cy="6" r="6" fill="#fff"/><path d="M4 3.2l1 1.6-.6.7c.4.9 1 1.5 1.9 1.9l.7-.6 1.6 1-.6 1.2C6 8.8 3.2 6 3 3.8z" fill="#005753"/></svg>0749306417</div>
      </div>
      <span class="divider" aria-hidden="true"></span>
      <div class="practice practice--calliope">
        <div class="line">Calliope - Shop 3 42,</div>
        <div class="line">Pellow Drive</div>
        <div class="line"><svg class="icon" viewBox="0 0 12 12"><circle cx="6" cy="6" r="6" fill="#fff"/><path d="M4 3.2l1 1.6-.6.7c.4.9 1 1.5 1.9 1.9l.7-.6 1.6 1-.6 1.2C6 8.8 3.2 6 3 3.8z" fill="#005753"/></svg>49628473</div>
      </div>
    </div>
  </section>

  <section class="card card--back">
    <div class="side-band"><span class="side-name">Bluefern Dental</span></div>
    <span class="stripe stripe--a" aria-hidden="true"></span>
    <span class="stripe stripe--b" aria-hidden="true"></span>
    <span class="back-mark" aria-hidden="true"></span>
    <p class="back-tagline">Your Smile, My Passion..!</p>
  </section>
</body>
</html>
```